Honey apple cider vinegar label

organic food company need a contemporary honey apple cider vinegar and honey vinegar label, natural GMP logo HACCP LOgo
label detail height :140mm Width:80mm
ingredient: honey, apple cider vinegar and water, free from artificial color & preservative
Shelf Life: 3 years
Net weight 400ml
Storage : store in cool place , do not expose to sunlight
instruction for use: add 20ml to a full glass of water 3, times a days before meal, stop consuming if allergies happen
certification, GMP HACCP, Halal, natural product

Target Market(s)

health conscious group

Requirements
Must have
• modern feel, honey and apple picture

```html
<!DOCTYPE html>
<html lang="en">
<head>
<meta charset="utf-8">
<title>Orchava Honey Apple Cider Vinegar Label</title>
<link href="https://fonts.googleapis.com/css2?family=Playfair+Display:wght@400;700;800;900&display=swap" rel="stylesheet">
<style>
  :root {
    --plum: #351a45;
    --leaf-green: #8cc63f;
    --paper: #ffffff;
    --paper-shade: #eeeff1;
    --stage: #e9eaec;
    --apple-red: #a8182a;
    --honey: #e2a229;
  }
  * { margin: 0; padding: 0; box-sizing: border-box; }
  html, body { width: 1200px; height: 999px; overflow: hidden; }
  body { background: var(--stage); position: relative; font-family: "Playfair Display", serif; }

  .label {
    position: absolute; left: 332px; top: 33px;
    width: 535px; height: 933px; overflow: hidden;
    background: linear-gradient(115deg, var(--paper) 0%, var(--paper) 55%, var(--paper-shade) 75%, var(--paper) 100%);
    box-shadow: 0 6px 24px rgba(0,0,0,0.12);
  }
  .crest { position: absolute; left: 0; top: 0; width: 535px; height: 300px; }
  .brand-dot {
    position: absolute; left: 238px; top: 125px; width: 56px; height: 56px;
    border-radius: 50%; background: var(--plum);
  }
  .brand-name {
    position: absolute; left: 0; width: 535px; top: 222px; text-align: center;
    font-weight: 800; font-size: 46px; color: var(--plum); line-height: 1;
  }

  .info {
    position: absolute; top: 14px; color: var(--plum);
    font-size: 10px; line-height: 1.35; font-weight: 400;
  }
  .info b { font-weight: 700; }
  .info p + p { margin-top: 4px; }
  .info-left { left: 14px; width: 88px; }
  .info-right { left: 364px; width: 158px; }

  .product-photo {
    position: absolute; left: 70px; top: 510px; width: 465px; height: 370px;
    border-radius: 46% 40% 30% 38%;
    background: radial-gradient(ellipse at 30% 65%, var(--apple-red) 0%, #c23a3a 30%, transparent 55%),
                radial-gradient(ellipse at 62% 40%, var(--honey) 0%, #c98a3c 35%, transparent 62%),
                radial-gradient(ellipse at 70% 78%, #f4e3c2 0%, transparent 50%);
  }
  .title { position: absolute; left: 60px; width: 470px; font-weight: 700; line-height: 1; letter-spacing: -1px; }
  .title-honey { top: 296px; font-size: 150px; color: var(--plum); }
  .title-apple {
    top: 420px; font-size: 150px; color: var(--leaf-green);
    text-shadow: 3px 3px 0 var(--paper), -3px -3px 0 var(--paper), 3px -3px 0 var(--paper), -3px 3px 0 var(--paper);
  }
  .variant-pill {
    position: absolute; left: 100px; top: 792px; width: 334px; height: 52px;
    border-radius: 26px; background: var(--plum); color: var(--paper);
    font-weight: 700; font-size: 33px; text-align: center; line-height: 52px;
  }
  .volume-tab {
    position: absolute; left: 210px; top: 874px; width: 116px; height: 118px;
    border-radius: 58px; background: var(--plum); color: var(--paper);
    font-weight: 700; font-size: 20px; text-align: center; padding-top: 14px;
  }
  .cert-marks {
    position: absolute; left: 372px; top: 888px; display: flex; gap: 10px;
  }
  .cert-mark {
    width: 34px; height: 34px; border-radius: 50%;
    border: 3px solid var(--plum); background: var(--paper);
  }
</style>
</head>
<body>
  <main class="label">
    <svg class="crest" viewBox="0 0 535 300" aria-hidden="true">
      <rect x="112" y="0" width="241" height="110" fill="#351a45"/>
      <path d="M140 284 A132 132 0 0 1 402 284" fill="#ffffff" stroke="#351a45" stroke-width="8"/>
      <rect x="112" y="0" width="241" height="96" fill="#351a45"/>
    </svg>
    <div class="brand-dot"></div>
    <div class="brand-name">orchava</div>

    <section class="info info-left">
      <p><b>Ingredients:</b> honey, apple cider vinegar, water.</p>
      <p>Free from artificial colour &amp; preservative.</p>
      <p><b>Shelf life:</b> 3 years</p>
    </section>
    <section class="info info-right">
      <p><b>Storage:</b> store in a cool place, do not expose to sunlight.</p>
      <p><b>Use:</b> add 20ml to a full glass of water, 3 times a day before meals. Stop if allergies occur.</p>
    </section>

    <div class="product-photo" role="img" aria-label="Photo of a red apple, an apple slice and a wooden honey dipper dripping honey"></div>

    <h1 class="title title-honey">honey</h1>
    <div class="title title-apple">apple</div>

    <div class="variant-pill">CIDER VINEGAR</div>
    <div class="volume-tab">400ml</div>

    <div class="cert-marks" role="img" aria-label="GMP, HACCP, Halal and natural product certification marks">
      <span class="cert-mark"></span>
      <span class="cert-mark"></span>
      <span class="cert-mark"></span>
      <span class="cert-mark"></span>
    </div>
  </main>
</body>
</html>
```